Need a book cover design for a Lumora Book on Herbal Remedies

I need a book cover for my new ebook, here are the details:
Title: Meadow Cures
Sub-Heading: Buried Ancient Garden Tonics
Reclaiming the Wisdom of Roots for Everyday Wellness and Strength
Author: Nora Belcourt

```html
<!DOCTYPE html>
<html lang="en">
<head>
<meta charset="UTF-8">
<title>Meadow Cures — Book Cover</title>
<link href="https://fonts.googleapis.com/css2?family=Abril+Fatface&family=Outfit:wght@500;600;700&display=swap" rel="stylesheet">
<style>
  :root {
    --page-bg: #f3f5f1;
    --cover-sage: #d6e2cf;
    --cover-sage-light: #e3ecdc;
    --leaf-grey: #9fb5a8;
    --leaf-deep: #7f9c8b;
    --ink-green: #2f6b40;
    --ink-dark: #1f4a2e;
    --halo: #f4f8f0;
    --herb-green: #5f9a55;
    --lavender: #8c7fbf;
    --stone: #8d8f99;
  }
  * { margin: 0; padding: 0; box-sizing: border-box; }
  html, body {
    width: 1200px; height: 1200px; overflow: hidden;
    background: var(--page-bg);
  }
  .book-cover {
    position: absolute;
    left: 220px; top: 30px;
    width: 760px; height: 1140px;
    overflow: hidden;
    background: var(--cover-sage);
    box-shadow: 0 6px 24px rgba(40, 60, 45, 0.18);
  }
  .leaf-frame {
    position: absolute; inset: 0;
    background:
      radial-gradient(ellipse 62% 58% at 50% 50%, var(--cover-sage-light) 0%, var(--cover-sage) 70%, rgba(214,226,207,0) 100%),
      linear-gradient(135deg, var(--leaf-grey) 0%, var(--cover-sage) 30%, var(--cover-sage) 70%, var(--leaf-deep) 100%);
  }
  .herb-illustration {
    position: absolute;
    left: 80px; top: 300px;
    width: 620px; height: 610px;
    border-radius: 46% 46% 40% 40%;
    background:
      radial-gradient(circle at 70% 80%, rgba(141,143,153,0.75) 0 18%, transparent 19%),
      radial-gradient(ellipse at 30% 55%, rgba(140,127,191,0.35) 0 20%, transparent 45%),
      radial-gradient(ellipse at 50% 60%, rgba(95,154,85,0.75) 0 35%, rgba(95,154,85,0) 68%);
  }
  .cover-text {
    position: absolute; left: 0; width: 100%;
    text-align: center;
    color: var(--ink-dark);
    text-shadow:
      2px 0 0 var(--halo), -2px 0 0 var(--halo),
      0 2px 0 var(--halo), 0 -2px 0 var(--halo),
      2px 2px 0 var(--halo), -2px -2px 0 var(--halo),
      2px -2px 0 var(--halo), -2px 2px 0 var(--halo);
  }
  .series-label {
    top: 72px;
    font-family: "Outfit", sans-serif;
    font-weight: 600;
    font-size: 22px;
  }
  .book-title {
    top: 110px;
    font-family: "Abril Fatface", serif;
    font-weight: 400;
    font-size: 138px;
    line-height: 0.98;
    color: var(--ink-green);
    text-shadow:
      4px 0 0 var(--halo), -4px 0 0 var(--halo),
      0 4px 0 var(--halo), 0 -4px 0 var(--halo),
      3px 3px 0 var(--halo), -3px -3px 0 var(--halo),
      3px -3px 0 var(--halo), -3px 3px 0 var(--halo);
  }
  .book-subtitle {
    top: 920px;
    font-family: "Outfit", sans-serif;
    font-weight: 600;
    font-size: 29px;
    line-height: 1.4;
  }
  .author-name {
    top: 1060px;
    font-family: "Outfit", sans-serif;
    font-weight: 700;
    font-size: 42px;
    letter-spacing: 0.5px;
  }
</style>
</head>
<body>
  <main class="book-cover">
    <div class="leaf-frame" role="img" aria-label="Soft sage background with a border of grey-green leafy herb sprigs"></div>
    <div class="herb-illustration" role="img" aria-label="Watercolour bouquet of rosemary, lavender, chamomile and daisies beside a grey stone mortar and pestle"></div>
    <p class="cover-text series-label">Buried Ancient Garden Tonics</p>
    <h1 class="cover-text book-title">Meadow<br>Cures</h1>
    <p class="cover-text book-subtitle">Reclaiming the Wisdom of Roots<br>for Everyday Wellness and Strength</p>
    <p class="cover-text author-name">NORA BELCOURT</p>
  </main>
</body>
</html>
```